Quilled Mark website redesign

We have an existing website www.QuilledMarkSubtitles.com that needs design improvements and modernization. We want to keep the basic idea of the pop art and the dialogue balloons.

Target Market(s)

US and Europe media producers

Industry/Entity Type

Media

Coding

Coded - Design and coding required

Number of Pages Required

5+ page

Font styles to use
Other font styles liked:
• Modern font

Requirements
Must have
• current pop art figures, current logo,
Nice to have
• I like the idea of the current website. It just needs improvments and modernization.
Should not have
• No movement necessary

```html
<!DOCTYPE html>
<html lang="en">
<head>
<meta charset="utf-8">
<title>Quilled Mark – Closed Captioning</title>
<link href="https://fonts.googleapis.com/css2?family=Parisienne&family=Raleway:wght@400;500;600;700&display=swap" rel="stylesheet">
<style>
:root{
  --yellow:#f2c81f;
  --yellow-deep:#e9b914;
  --ink:#111111;
  --text:#333333;
  --muted:#666666;
  --white:#ffffff;
  --soft:#f4f4f4;
  --footer:#262626;
  --pink:#e63d8a;
  --blue:#2a7bd6;
}
*{margin:0;padding:0;box-sizing:border-box}
html,body{width:1200px;height:4655px;overflow:hidden}
body{position:relative;font-family:"Raleway",sans-serif;color:var(--text);background:var(--white)}
.abs{position:absolute}
.script{font-family:"Parisienne",cursive;font-weight:400;color:var(--ink)}
.btn-dark{background:var(--ink);color:var(--white);font-weight:600;font-size:16px;letter-spacing:1px;display:flex;align-items:center;justify-content:center}
.btn-yellow{background:var(--yellow);color:var(--ink);font-weight:700;font-size:15px;letter-spacing:1px;display:flex;align-items:center;justify-content:center}

/* top bar */
.topbar{top:0;left:0;width:1200px;height:42px;display:flex;align-items:center;font-size:13px;color:var(--ink)}
.topbar span{position:absolute;display:flex;align-items:center;gap:10px}
/* nav */
.nav{top:42px;left:0;width:1200px;height:86px;background:var(--yellow)}
.brand{left:126px;top:14px;width:105px;height:58px;background:var(--yellow-deep);border:2px solid var(--white);display:flex;align-items:center;justify-content:center;font-weight:700;font-size:14px;color:var(--ink);text-align:center;line-height:1.1}
.menu{left:296px;top:30px;display:flex;gap:35px;font-size:16px;color:var(--white);font-weight:500}
.menu .active{border-bottom:2px solid var(--white);padding-bottom:6px}
.nav .btn-dark{left:953px;top:23px;width:143px;height:43px;font-size:16px}

/* hero */
.hero-art{left:0;top:200px;width:632px;height:572px;background:linear-gradient(160deg,#f3c7a3 0%,#d23a2e 55%,#2b2b6b 100%);border-radius:0 260px 0 0}
.hero-title{right:112px;top:272px;font-size:60px;line-height:1;text-align:right}
.hero-lines{right:112px;top:396px;text-align:right;font-size:24px;line-height:41px;color:var(--text)}
.hero .btn-dark{left:945px;top:546px;width:141px;height:43px}
.arrow-circle{width:32px;height:32px;border:1.5px solid var(--ink);border-radius:50%;display:flex;align-items:center;justify-content:center;background:var(--white)}
.dots{display:flex;gap:6px}
.dots i{width:8px;height:8px;border-radius:50%;background:#bbb;display:block}
.dots i.on{background:var(--ink)}

/* why section */
.why{top:772px;left:0;width:1200px;height:986px;background:linear-gradient(180deg,var(--yellow),var(--yellow-deep))}
.why h2{position:absolute;top:70px;width:1200px;text-align:center;font-size:52px}
.why h3{position:absolute;top:150px;width:1200px;text-align:center;font-size:26px;font-weight:500;color:var(--ink)}
.feature{top:243px;width:249px;height:358px;background:var(--white);border-bottom:7px solid var(--ink);text-align:center;box-shadow:0 4px 10px rgba(0,0,0,.12)}
.feature .icon{margin:26px auto 0;width:100px;height:100px;border-radius:50%;border:7px solid var(--yellow);display:flex;align-items:center;justify-content:center}
.feature h4{font-family:"Parisienne",cursive;font-weight:400;font-size:21px;line-height:22px;margin-top:20px;color:var(--ink);height:46px}
.feature p{font-size:14px;line-height:21px;color:var(--text);margin-top:10px;height:70px}
.feature .btn-yellow{position:absolute;left:64px;top:293px;width:122px;height:34px;font-size:14px;font-weight:500}
.why .body{position:absolute;left:118px;top:646px;width:964px;text-align:center;font-size:17px;line-height:26px;color:#3a3000}
.why .body p+p{margin-top:26px}
.why .btn-dark{left:527px;top:869px;width:145px;height:39px}

/* services */
.services h2{position:absolute;top:1825px;width:1200px;text-align:center;font-size:48px}
.service{top:1935px;width:289px;height:392px;background:var(--white);box-shadow:0 2px 12px rgba(0,0,0,.1);text-align:center}
.service .icon{margin:48px auto 0;width:118px;height:96px;border:7px solid var(--yellow);display:flex;align-items:center;justify-content:center}
.service h4{font-family:"Parisienne",cursive;font-weight:400;font-size:24px;line-height:26px;color:var(--muted);margin-top:22px;height:60px}
.service p{font-size:13px;line-height:26px;color:var(--muted);padding:0 20px;height:86px}
.service .btn-yellow{margin:8px auto 0;width:124px;height:36px;font-size:14px}

/* testimonials */
.testi-head{top:2412px;left:0;width:1200px;height:174px;background:var(--soft)}
.testi-head h2{position:absolute;top:78px;width:1200px;text-align:center;font-size:48px}
.testi-art{top:2586px;left:0;width:1200px;height:564px;background:radial-gradient(circle at 50% 50%,#f07ab0 0%,var(--pink) 55%,#c42a6e 100%)}
.cloud{top:2690px;left:270px;width:660px;height:330px;background:var(--white);border:6px solid #a8124f;border-radius:160px}
.quote{top:2748px;left:270px;width:660px;text-align:center;font-size:20px;line-height:41.5px;color:var(--ink);font-weight:500;white-space:nowrap}

/* clients */
.clients h2{position:absolute;top:3218px;width:1200px;text-align:center;font-size:46px}
.client{top:3310px;width:200px;height:98px;background:var(--white);box-shadow:0 2px 10px rgba(0,0,0,.15);border-radius:6px;display:flex;align-items:center;justify-content:center;text-align:center;font-weight:700;font-size:18px;color:#1d3e7a;padding:0 12px}

/* mailing */
.mailing{top:3529px;left:0;width:1200px;height:255px;background:var(--yellow)}
.mailing h2{position:absolute;top:40px;width:1200px;text-align:center;font-size:46px}
.mailing p{position:absolute;top:106px;width:1200px;text-align:center;font-size:20px;color:var(--ink)}
.mail-form{left:400px;top:155px;width:402px;height:42px;display:flex}
.mail-form .field{flex:1;background:var(--ink);color:var(--white);font-size:16px;display:flex;align-items:center;padding-left:18px}
.mail-form .go{width:106px;border:2px solid var(--ink);display:flex;align-items:center;justify-content:center;font-size:18px;color:var(--ink);font-weight:500}

/* contact */
.contact-art{top:3784px;left:650px;width:550px;height:519px;background:linear-gradient(135deg,#f2f2f2,#9a9a9a 60%,#5a5a5a)}
.contact h2{position:absolute;top:3830px;left:235px;font-size:46px}
.label{font-size:14px;color:var(--ink);font-weight:500}
.input{height:41px;border:1.5px solid #777;background:var(--white)}
.robot{left:56px;top:4214px;width:214px;height:60px;border:1px solid #ddd;background:#f9f9f9;display:flex;align-items:center;gap:10px;padding-left:12px;font-size:11px;color:var(--ink)}
.robot i{width:22px;height:22px;border:2px solid #c1c1c1;background:var(--white);display:block}
.send{left:420px;top:4234px;width:176px;height:42px;background:var(--yellow);color:var(--ink);font-size:18px;font-weight:500;display:flex;align-items:center;justify-content:center}

/* footer */
.footer{top:4303px;left:0;width:1200px;height:352px;background:var(--footer);color:#e6e6e6}
.footer .brand{left:90px;top:77px;width:139px;height:69px;font-size:18px}
.socials{left:72px;top:184px;display:flex;gap:22px}
.socials i{width:14px;height:14px;border-radius:50%;background:#e6e6e6;display:block}
.fcol{top:58px}
.fcol h5{font-family:"Parisienne",cursive;font-weight:400;font-size:24px;color:var(--white);margin-bottom:20px}
.fcol li{list-style:none;font-size:17px;line-height:41px}
.fcontact li{display:flex;gap:14px;align-items:flex-start;line-height:24px;margin-bottom:18px}
.fline{left:86px;top:283px;width:1067px;height:1px;background:#777}
.copy{top:308px;width:1200px;text-align:center;font-size:17px}
.fcode{right:50px;top:306px;font-size:14px}
</style>
</head>
<body>

<!-- Top bar -->
<div class="abs topbar">
  <span style="left:108px"><svg width="22" height="16" viewBox="0 0 22 16"><rect x="1" y="1" width="20" height="14" fill="none" stroke="#111" stroke-width="1.6"/><path d="M1 1l10 8 10-8" fill="none" stroke="#111" stroke-width="1.6"/></svg>TalkToUs@QuilledMarkSubtitles.com</span>
  <span style="left:498px"><svg width="16" height="16" viewBox="0 0 24 24"><path d="M5 3l4 1 2 5-3 2a12 12 0 0 0 5 5l2-3 5 2 1 4-3 2C10 21 3 14 3 6z" fill="none" stroke="#111" stroke-width="1.8"/></svg>Phone:(301) 555-0147</span>
  <span style="left:884px"><svg width="16" height="16" viewBox="0 0 24 24"><circle cx="12" cy="12" r="10" fill="none" stroke="#111" stroke-width="2"/><path d="M12 6v6l4 2" fill="none" stroke="#111" stroke-width="2"/></svg>Mon - Sat : 08.00-21.00</span>
</div>

<!-- Navigation -->
<header class="abs nav">
  <div class="abs brand">Quilled<br>Mark</div>
  <nav class="abs menu">
    <span class="active">Home</span><span>Services</span><span>Samples and Prices</span><span>Blog</span><span>About Us</span><span>Talk To Us</span>
  </nav>
  <div class="abs btn-dark">CONTACT</div>
</header>

<!-- Hero -->
<section class="hero">
  <div class="abs hero-art" role="img" aria-label="Pop art illustration of a surprised bearded man in a red shirt pointing at the headline"></div>
  <h1 class="abs script hero-title">We Create Broadcast<br>Quality</h1>
  <div class="abs hero-lines">Closed Captioning and Subtilting<br>CCSL and Dialogue Lists<br>Audio Description</div>
  <div class="abs btn-dark">BOOK NOW</div>
  <div class="abs arrow-circle" style="left:40px;top:423px"><svg width="12" height="12" viewBox="0 0 12 12"><path d="M8 1L3 6l5 5" fill="none" stroke="#111" stroke-width="1.6"/></svg></div>
  <div class="abs arrow-circle" style="left:1128px;top:423px"><svg width="12" height="12" viewBox="0 0 12 12"><path d="M4 1l5 5-5 5" fill="none" stroke="#111" stroke-width="1.6"/></svg></div>
  <div class="abs dots" style="left:564px;top:713px"><i></i><i></i><i class="on"></i><i></i><i></i></div>
</section>

<!-- Why us -->
<section class="abs why">
  <h2 class="script">Closed Captioning Since 2003</h2>
  <h3>Why it makes better sense to do Closed Captioning and CCSL</h3>

  <div class="abs feature" style="left:69px">
    <div class="icon"><svg width="44" height="54" viewBox="0 0 44 54"><rect x="4" y="2" width="36" height="50" rx="3" fill="var(--blue)"/><circle cx="22" cy="24" r="8" fill="var(--yellow)"/></svg></div>
    <h4>Post Production<br>Script</h4>
    <p>CCSL<br>Dialogue List<br>As Broadcast Script</p>
    <div class="btn-yellow">VISITE</div>
  </div>
  <div class="abs feature" style="left:340px">
    <div class="icon"><svg width="58" height="48" viewBox="0 0 58 48"><rect x="2" y="6" width="46" height="32" rx="3" fill="var(--blue)"/><rect x="20" y="38" width="10" height="6" fill="#555"/><rect x="34" y="2" width="22" height="16" rx="2" fill="#5ec6e8"/></svg></div>
    <h4>Closed<br>Captioning</h4>
    <p>Broadcast Quality<br>Offline Captioning<br>Live Captioning</p>
    <div class="btn-yellow">VISITE</div>
  </div>
  <div class="abs feature" style="left:611px">
    <div class="icon"><svg width="56" height="42" viewBox="0 0 56 42"><rect x="2" y="2" width="52" height="38" rx="3" fill="#3b6fd1"/><rect x="12" y="24" width="32" height="5" fill="#fff"/></svg></div>
    <h4>Subtitling</h4>
    <p>Over 60 translators<br>Over 20 languages</p>
    <div class="btn-yellow">VISITE</div>
  </div>
  <div class="abs feature" style="left:882px">
    <div class="icon"><svg width="40" height="56" viewBox="0 0 40 56"><rect x="10" y="2" width="20" height="32" rx="10" fill="#8fb9e8"/><path d="M4 26a16 16 0 0 0 32 0M20 42v10" fill="none" stroke="#555" stroke-width="3"/></svg></div>
    <h4>Audio<br>Description</h4>
    <p>English<br>Spanish<br>Audio and Video Files</p>
    <div class="btn-yellow">VISITE</div>
  </div>

  <div class="body">
    <p>Since 2003, Quilled Mark has been providing broadcast quality Closed Captioning, Subtitling, Post Production Scripts such as CCSL, Dialogue List and Audio Description services to the Film and Television Industry in the US and worldwide.</p>
    <p>We are quick, accurate and inexpensive and understand that when it comes to delivering your final movie to the network of film distributor, it's not just closed captioning but also a continuity or a dialogue list that needs to go with it.</p>
  </div>
  <div class="abs btn-dark">READ MORE</div>
</section>

<!-- Services -->
<section class="services">
  <h2 class="script">Our Services</h2>
  <div class="abs arrow-circle" style="left:40px;top:2108px"><svg width="12" height="12" viewBox="0 0 12 12"><path d="M8 1L3 6l5 5" fill="none" stroke="#111" stroke-width="1.6"/></svg></div>
  <div class="abs arrow-circle" style="left:1128px;top:2108px"><svg width="12" height="12" viewBox="0 0 12 12"><path d="M4 1l5 5-5 5" fill="none" stroke="#111" stroke-width="1.6"/></svg></div>

  <div class="abs service" style="left:110px">
    <div class="icon"><svg width="58" height="48" viewBox="0 0 58 48"><rect x="2" y="6" width="46" height="32" rx="3" fill="var(--blue)"/><rect x="20" y="38" width="10" height="6" fill="#555"/><rect x="34" y="2" width="22" height="16" rx="2" fill="#5ec6e8"/></svg></div>
    <h4>Closed Captioning &amp;<br>Subtitling Services</h4>
    <p>Fast, Accurate, and Inexpensive Broadcast Quality Offline, Live, and Experienced with StreamCo...</p>
    <div class="btn-yellow">READ MORE</div>
  </div>
  <div class="abs service" style="left:455px">
    <div class="icon"><svg width="40" height="54" viewBox="0 0 44 54"><rect x="4" y="2" width="36" height="50" rx="3" fill="var(--blue)"/><circle cx="22" cy="24" r="8" fill="var(--yellow)"/></svg></div>
    <h4>Post Production Scripts</h4>
    <p>Highly Detailed Post Production Scripts - CCSL, CDSL, ABS, Dialogue &amp; Spotting Lists</p>
    <div class="btn-yellow">READ MORE</div>
  </div>
  <div class="abs service" style="left:797px">
    <div class="icon"><svg width="40" height="56" viewBox="0 0 40 56"><rect x="10" y="2" width="20" height="32" rx="10" fill="#8fb9e8"/><path d="M4 26a16 16 0 0 0 32 0M20 42v10" fill="none" stroke="#555" stroke-width="3"/></svg></div>
    <h4>Audio<br>Description</h4>
    <p>Closed Captioning and Subtitling to mp2, .mov pro-res, .wmv High-End Encoding and Delivery of Captioning.</p>
    <div class="btn-yellow">READ MORE</div>
  </div>
</section>

<!-- Testimonials -->
<section>
  <div class="abs testi-head"><h2 class="script">Our Testimonials</h2></div>
  <div class="abs testi-art" role="img" aria-label="Pop art banner with two comic-style women and WOW and OMG speech bursts on a pink halftone background"></div>
  <div class="abs cloud"></div>
  <blockquote class="abs quote">“Quilled Mark is a dream vendor, providing captioning and<br>transcription services to meet our often tight deadlines. The<br>whole team is responsive, flexible, consistent and fun to work<br>with!” Dana Whitlow, BRIGHTREEL Mara and her team are my<br>go-to deliverables team on all our movies! They are</blockquote>
  <div class="abs arrow-circle" style="left:74px;top:2866px;border-color:#fff;background:#111"><svg width="14" height="12" viewBox="0 0 14 12"><path d="M13 6H2M6 1L1 6l5 5" fill="none" stroke="#fff" stroke-width="1.6"/></svg></div>
  <div class="abs arrow-circle" style="left:1050px;top:2866px;border-color:#111;background:#fff"><svg width="14" height="12" viewBox="0 0 14 12"><path d="M1 6h11M8 1l5 5-5 5" fill="none" stroke="#111" stroke-width="1.6"/></svg></div>
  <div class="abs dots" style="left:564px;top:2983px"><i></i><i></i><i class="on"></i><i></i><i></i></div>
</section>

<!-- Clients -->
<section class="clients">
  <h2 class="script">Our Clients</h2>
  <div class="abs client" style="left:114px">Harvest Valley TV</div>
  <div class="abs client" style="left:372px">Summit Crest Studios</div>
  <div class="abs client" style="left:627px;color:#c0161c">Framecut</div>
  <div class="abs client" style="left:885px">Northbay Film Guild</div>
  <svg class="abs" style="left:540px;top:3460px" width="36" height="22" viewBox="0 0 36 22"><path d="M34 11H3M11 2L2 11l9 9" fill="none" stroke="#111" stroke-width="2.5"/></svg>
  <svg class="abs" style="left:618px;top:3460px" width="36" height="22" viewBox="0 0 36 22"><path d="M2 11h31M25 2l9 9-9 9" fill="none" stroke="#111" stroke-width="2.5"/></svg>
</section>

<!-- Mailing list -->
<section class="abs mailing">
  <h2 class="script">Join Our Mailing List</h2>
  <p>For receiving our news and updates in your inbox directly.</p>
  <div class="abs mail-form"><div class="field">Your Email Address</div><div class="go">SIGN UP</div></div>
</section>

<!-- Contact -->
<section class="contact">
  <h2 class="script">Contact Us</h2>
  <div class="abs label" style="left:56px;top:3930px">FIRST NAME</div>
  <div class="abs input" style="left:56px;top:3958px;width:258px"></div>
  <div class="abs label" style="left:340px;top:3930px">LAST NAME</div>
  <div class="abs input" style="left:340px;top:3958px;width:258px"></div>
  <div class="abs label" style="left:56px;top:4021px">E-MAIL ADDRESS</div>
  <div class="abs input" style="left:56px;top:4049px;width:542px"></div>
  <div class="abs label" style="left:56px;top:4112px">MESSAGE</div>
  <div class="abs input" style="left:56px;top:4140px;width:542px"></div>
  <div class="abs robot"><i></i>I'm not a robot</div>
  <div class="abs send">SEND</div>
  <div class="abs contact-art" role="img" aria-label="Black and white pop art drawing of a woman with flowing hair"></div>
</section>

<!-- Footer -->
<footer class="abs footer">
  <div class="abs brand">Quilled<br>Mark</div>
  <div class="abs socials"><i></i><i></i><i></i><i></i><i></i></div>

  <div class="abs fcol" style="left:314px">
    <h5>About</h5>
    <ul><li>Closed Captioning</li><li>Subtitling Services</li><li>Post Production Scripts</li><li>Audio Description</li></ul>
  </div>
  <div class="abs fcol" style="left:575px">
    <h5>Our Net works</h5>
    <ul><li>About Us</li><li>Talk To Us</li><li>Privacy Policy</li><li>Services</li></ul>
  </div>
  <div class="abs fcol fcontact" style="left:786px">
    <h5>Contacts</h5>
    <ul>
      <li><svg width="18" height="24" viewBox="0 0 18 24"><path d="M9 1a8 8 0 0 0-8 8c0 6 8 14 8 14s8-8 8-14a8 8 0 0 0-8-8z" fill="#e6e6e6"/><circle cx="9" cy="9" r="3" fill="#262626"/></svg><span>Quilled Mark, LLC 120 Linden Ave,<br>MD 20899</span></li>
      <li><svg width="20" height="16" viewBox="0 0 22 16"><rect x="1" y="1" width="20" height="14" fill="none" stroke="#e6e6e6" stroke-width="1.6"/><path d="M1 1l10 8 10-8" fill="none" stroke="#e6e6e6" stroke-width="1.6"/></svg><span>TalkToUs@QuilledMarkSubtitles.com</span></li>
      <li><svg width="20" height="20" viewBox="0 0 24 24"><path d="M5 3l4 1 2 5-3 2a12 12 0 0 0 5 5l2-3 5 2 1 4-3 2C10 21 3 14 3 6z" fill="none" stroke="#e6e6e6" stroke-width="1.8"/></svg><span>(301) 555-0147</span></li>
    </ul>
  </div>
  <div class="abs fline"></div>
  <div class="abs copy">Copyright © 2024 &nbsp;QUILLED MARK. All Rights Reserved</div>
  <div class="abs fcode">C75</div>
</footer>

</body>
</html>
```